Healing Arts Brochure with Simple, Elegant, Zen Design ,

I need to create a brochure for an upcoming event and I have to complete this project in the next few days.
I would like a tri-fold or z fold type of brochure- standard size of 8.5 x 11- both sides with text

i would like the overall design to be simple, elegant and zen .... yet not too plain :-))
I would like the fonts used to be clean and clear and ... easy to read.
I would like the background color to be white/cream or light color
Please do not use too many colors when working with the descriptions of my services or break those sections up too much ... a little is ok.
I don't want the brochure to be busy

I've uploaded the text, my photo, a photo that I will be using on my website, my logo symbol without my name and several logo symbols with my name in different font styles. I am not wed to any of the various font styles of the logo just yet.
TEXT FILE IS UPLOADED
Updates

Dear Designers, The design submissions that I'm receiving so far have not been including all 3 pages of text in the brochure. I pulled my text file to update it with the instructions that there are 3 pages of text information that need to be on the brochure. Unfortunately, I'm not able to upload the text file - seems to be a glitch on the PixelTorch website.. I called for support and they won't get back to me for a couple of hours. That will be around 11:00 am PST in the USA. PLEASE CHECK BACK if you haven't already downloaded the text file. Otherwise, please add the missing information and resubmit your ideas. Thank you!! RM

Target Market(s)

My services target clients in the healing arts.

Industry/Entity Type

Event

Requirements
Must have
• Please include the colors tones of my logo and the sunset photo -golds, oranges, blues
Brochure must include my photo and the sunset photo
Should not have
• Objects like teacups etc. that have nothing to do with my services - thank you kindly
I don't want any other photos or objects on the brochure other than my photo and the sun
Please don't put the tagline in quotes
Please do not make the brochure busy with too many colors in the text.

```html
<!DOCTYPE html>
<html lang="en">
<head>
<meta charset="utf-8">
<title>Maren Vale – Healing Arts Brochure</title>
<link href="https://fonts.googleapis.com/css2?family=Montserrat:wght@400;500;600;700&family=Mulish:wght@400;500;600&display=swap" rel="stylesheet">
<style>
:root{
  --bg:#e6e6e6;
  --paper:#ffffff;
  --paper-shade:#eef0f2;
  --orange:#e8761c;
  --orange-deep:#d86a12;
  --blue:#2f5d9c;
  --ink:#222222;
  --grey:#7a7a7a;
  --photo-skin:#d8b7a0;
  --photo-grey:#bfbfbf;
  --pool:#3d9ad0;
}
*{box-sizing:border-box;margin:0;padding:0}
html,body{width:1200px;height:1000px;overflow:hidden}
body{background:var(--bg);font-family:"Mulish",sans-serif;color:var(--ink);position:relative}
.brochure{position:absolute;left:60px;top:82px;width:1080px;height:836px;display:flex;box-shadow:0 6px 24px rgba(0,0,0,.18)}
.panel{width:360px;height:100%;position:relative;overflow:hidden}

/* Panel 1 */
.panel--intro{background:var(--paper)}
.intro__halo{position:absolute;left:-40px;top:-60px;width:380px;height:380px;border-radius:50%;background:radial-gradient(circle at 45% 40%,#ffffff 55%,var(--paper-shade) 100%);box-shadow:0 2px 10px rgba(0,0,0,.08)}
.intro__portrait{position:absolute;left:22px;top:20px;width:128px;height:128px;border-radius:50%;background:radial-gradient(circle at 50% 45%,#c9a58c 0%,#8a6e58 60%,#4b5a3a 100%)}
.intro__name{position:absolute;right:16px;top:138px;font-family:"Montserrat",sans-serif;font-weight:600;font-size:20px;color:var(--ink);white-space:nowrap}
.intro__name small{font-size:12px;font-weight:400;color:var(--orange);margin-left:4px}
.intro__creds{position:absolute;left:50px;top:176px;font-size:12.5px;line-height:1.22;color:var(--grey)}
.intro__lead{position:absolute;left:24px;right:20px;top:264px;font-size:14.3px;line-height:1.15;color:var(--orange);font-weight:600}
.intro__body{position:absolute;left:24px;right:20px;top:396px}
.section-title{font-family:"Montserrat",sans-serif;font-weight:700;color:var(--blue);font-size:19px;margin-bottom:8px}
.body-text{font-size:13.6px;line-height:1.17;text-align:justify}
.sub-title{font-family:"Montserrat",sans-serif;font-weight:700;color:var(--blue);font-size:14px;line-height:1.2;margin:18px 0 8px}
.symptom-list{list-style:none;font-size:12.6px;line-height:1.22;color:#444}

/* Panel 2 */
.panel--sessions{background:linear-gradient(180deg,var(--orange) 0%,var(--orange-deep) 100%);border-left:1px solid #cfcfcf;border-right:1px solid #cfcfcf}
.sessions__photo{position:absolute;left:0;top:0;width:100%;height:310px;background:linear-gradient(120deg,var(--photo-skin) 0%,#e6cbb6 45%,var(--photo-grey) 100%);border-bottom-right-radius:160px 60px}
.sessions__title{position:absolute;right:28px;top:20px;font-family:"Montserrat",sans-serif;font-weight:400;font-size:19px;line-height:1.05;color:#fff}
.sessions__title span{display:block;font-size:12px;font-weight:500;margin-top:3px}
.sessions__text{position:absolute;left:22px;right:22px;top:345px;color:#fff;font-size:13.6px;line-height:1.17;text-align:justify}
.sessions__text p+p{margin-top:14px}
.sessions__url{position:absolute;left:0;right:0;bottom:24px;text-align:center;font-size:11px;color:#f7d7b8}

/* Panel 3 */
.panel--irenew{background:linear-gradient(180deg,#f4f5f7 0%,#ffffff 40%,#eceef1 100%);padding:28px 22px 0 24px}
.panel--irenew .section-title{font-size:18px;line-height:1.05;margin-bottom:16px}
.irenew__text{font-size:14.4px;line-height:1.2}
.irenew__text p+p{margin-top:16px}
.irenew__photo{position:absolute;left:18px;right:18px;bottom:22px;height:238px;background:linear-gradient(180deg,#d9dde0 0%,#b9c2c8 30%,var(--pool) 55%,#2f7fb0 75%,#8a8378 100%)}
.irenew__label{position:absolute;left:20px;top:96px;font-family:"Montserrat",sans-serif;font-size:22px;color:#fff;line-height:1}
.irenew__label span{display:block;font-size:12px;margin-top:4px}
</style>
</head>
<body>
<main class="brochure">
  <section class="panel panel--intro">
    <div class="intro__halo"></div>
    <div class="intro__portrait" role="img" aria-label="Portrait photo of the practitioner"></div>
    <h1 class="intro__name">Maren Vale <small>CMT, SUP</small></h1>
    <p class="intro__creds">is a Somatic Unwinding™ Practitioner, SUP<br>Certified Level III iRenew® Teacher<br>Certified Sound Healing Practitioner -<br>Coastal Institute of Integral Studies<br>Certified Deep Breathwork Facilitator</p>
    <p class="intro__lead">The services that I offer focus on supporting self-care, self-empowerment and self-regulation. Healing is returning home to our inherent sense of resiliency, vitality and well-being. I am honored to work with you and support you in your own unique journey home to yourself.</p>
    <div class="intro__body">
      <h2 class="section-title">Somatic Unwinding™</h2>
      <p class="body-text">Somatic Unwinding is a body-oriented approach to resolving the symptoms of trauma and chronic stress. Sources of trauma are wide- ranging, including; accidents, falls, surgeries, injuries, sexual assault, rape; emotional, physical or sexual abuse; loss of a loved one; childhood neglect or abuse, difficult births, high fever, serious illness, natural disasters, violence and war.</p>
      <h3 class="sub-title">The symptoms of unresolved trauma can include:</h3>
      <ul class="symptom-list">
        <li>Depression or anxiety (including panic attacks)</li>
        <li>Hyper-vigilance</li>
        <li>Chronic pain of all kinds</li>
        <li>Sleep disorders</li>
        <li>Chronic tension</li>
        <li>Addictions of all kinds</li>
        <li>Migraines</li>
        <li>Gastrointestinal disorders Dissociation</li>
        <li>And many others</li>
      </ul>
    </div>
  </section>

  <section class="panel panel--sessions">
    <div class="sessions__photo" role="img" aria-label="Photo of hands resting on a client's shoulder during a bodywork session"></div>
    <h2 class="sessions__title">Somatic<br>Unwinding™<span>Sessions</span></h2>
    <div class="sessions__text">
      <p>Trauma occurs when the instinctual “high arousal” states of our survival responses (fight, flight and freeze) are unable to discharge, settle and regulate in response to threatening and overwhelming experiences. The result is that this highly charged energy remains stuck or “frozen” as an unresolved memory within the body.</p>
      <p>Somatic Unwinding sessions assist clients to reconnect to their bodies and to gently discharge the stuck or "frozen" energies of trauma so that resiliency, stability and vitality are restored. I offer both Somatic Unwinding™ bodywork and techniques in my private practice. I'm deeply inspired and grateful for the results that I've witnessed in my clients. Somatic Unwinding is remarkable in its ability to bring healing and relief to the fear, hopelessness and pain of trauma.</p>
    </div>
    <p class="sessions__url">www.marenvale.com</p>
  </section>

  <section class="panel panel--irenew">
    <h2 class="section-title">iRenew® &amp; Yoga Nidra<br>Meditation</h2>
    <div class="irenew__text body-text">
      <p>iRenew® (Integrated Renewal) is a modern adaption of an ancient meditation practice called Yoga Nidra (yogic sleep). iRenew® is a research based protocol that provides a systematic method for promoting healing, stress reduction and self-regulation. iRenew® is used in the treatment of trauma, P.T.S.D., and many stress related illnesses; such as insomnia, chronic pain, anxiety and depression.</p>
      <p>I offer individual sessions of iRenew® and personalized instruction in learning Yoga Nidra meditation. The deep relaxation of Yoga Nidra is very restorative as it allows for the release of physical, emotional and mental tension as your body rests in a reclined position. Yoga Nidra facilitates the ability to develop the “relaxation response” and it is one of the most highly effective methods of stress reduction.</p>
    </div>
    <div class="irenew__photo" role="img" aria-label="Photo of a person seated in meditation beside a pool">
      <p class="irenew__label">iRenew®<span>Sessions</span></p>
    </div>
  </section>
</main>
</body>
</html>
```